We are an integrated facilities management company.

We aggregate everything related to facilities maintenance. Repair-replacement of equipment and facility space materials from:
Asset gathering and tracking.
Vendor screening, contracting and management.
Service requirement development.
Work order processing and management.
Invoice reconciliation.
Vendor payment.
Reporting.
Capital equipment bids and project management.

Target Market(s)

Retail, hospitality, multi-family housing, long term healthcare.

Industry/Entity Type

Maintenance

Contact Information for Business Card

Professional and bold look. (see logo zip file)

Colors
3377b5
85abd2
cedeed

Requirements
Must have
• N/A
Nice to have
• N/A
Should not have
• N/A

```html
<!DOCTYPE html>
<html lang="en">
<head>
<meta charset="utf-8">
<title>Brightspan Facility Services – Business Card</title>
<link href="https://fonts.googleapis.com/css2?family=Montserrat:wght@700;800&family=Roboto:wght@400;500&display=swap" rel="stylesheet">
<style>
  :root {
    --backdrop: #1e1e1e;
    --brand-blue: #1455a5;
    --slate: #666868;
    --ink-grey: #555555;
    --card-white: #ffffff;
    --band-text: #ffffff;
  }
  * { box-sizing: border-box; margin: 0; padding: 0; }
  html, body {
    width: 1200px; height: 900px; overflow: hidden;
    background: var(--backdrop);
    font-family: "Roboto", Arial, sans-serif;
  }
  .canvas { position: relative; width: 1200px; height: 900px; }

  .card {
    position: absolute; left: 290px; width: 620px; height: 355px;
    overflow: hidden;
  }

  /* Front */
  .card--front { top: 70px; background: var(--slate); }
  .front-brand {
    position: absolute; top: 0; left: 0; right: 0; height: 200px;
    display: flex; align-items: center; justify-content: center; gap: 14px;
  }
  .brand-dot { width: 22px; height: 22px; border-radius: 50%; background: var(--brand-blue); flex: none; }
  .front-brand .brand-name {
    font-family: "Montserrat", Arial, sans-serif; font-weight: 800;
    font-size: 30px; color: #ffffff; letter-spacing: 0.5px; text-transform: uppercase;
  }
  .service-band {
    position: absolute; top: 200px; left: 0; right: 0; bottom: 0;
    background: var(--brand-blue);
    display: flex; flex-direction: column; justify-content: center; align-items: center;
    text-align: center; color: var(--band-text);
    font-size: 14.5px; font-weight: 500; letter-spacing: 1.1px; line-height: 1.6;
  }

  /* Back */
  .card--back { top: 470px; background: var(--card-white); }
  .back-brand {
    position: absolute; top: 40px; left: 48px;
    display: flex; align-items: center; gap: 12px;
  }
  .back-brand .brand-name {
    font-family: "Montserrat", Arial, sans-serif; font-weight: 800;
    font-size: 22px; color: var(--brand-blue); text-transform: uppercase; letter-spacing: 0.3px;
  }
  .contact-list {
    position: absolute; top: 108px; left: 50px; list-style: none;
    color: var(--ink-grey); font-size: 19px; line-height: 1.6;
  }
  .contact-list li { display: flex; align-items: center; gap: 10px; }
  .contact-list svg { width: 20px; height: 20px; flex: none; }
  .web-highlight { color: var(--brand-blue); }
  .postal-address {
    position: absolute; top: 282px; left: 50px;
    color: var(--ink-grey); font-size: 20px; letter-spacing: 0.5px;
  }
  .person {
    position: absolute; top: 214px; right: 60px; text-align: right;
  }
  .person-name {
    font-family: "Montserrat", Arial, sans-serif; font-weight: 700;
    font-size: 28px; color: var(--brand-blue); letter-spacing: 1.5px; line-height: 1.2;
  }
  .person-role { font-size: 20px; color: var(--ink-grey); margin-top: 2px; }
  .corner-stripes { position: absolute; right: 0; bottom: 0; width: 150px; height: 100px; }
</style>
</head>
<body>
<main class="canvas">

  <section class="card card--front" aria-label="Card front">
    <div class="front-brand">
      <span class="brand-dot"></span>
      <span class="brand-name">Brightspan Facility Services</span>
    </div>
    <div class="service-band">
      <p>Asset gathering and tracking | Vendor screening, contracting and management</p>
      <p>Service requirement development | Work order processing and management</p>
      <p>Invoice reconciliation | Vendor payment | Reporting</p>
      <p>Capital equipment bids and project management</p>
    </div>
  </section>

  <section class="card card--back" aria-label="Card back">
    <div class="back-brand">
      <span class="brand-dot"></span>
      <span class="brand-name">Brightspan Facility Services</span>
    </div>

    <ul class="contact-list">
      <li>
        <svg viewBox="0 0 24 24" fill="none" stroke="#1455a5" stroke-width="2"><circle cx="12" cy="12" r="10"/><path d="M8.5 7.5l2 2-1 1.5c.8 1.6 1.9 2.7 3.5 3.5l1.5-1 2 2-1.5 1.5c-3.5-.5-6.5-3.5-7-7z"/></svg>
        555-014-2290
      </li>
      <li>
        <svg viewBox="0 0 24 24" fill="none" stroke="#1455a5" stroke-width="2"><rect x="2" y="5" width="20" height="14"/><path d="M2 5l10 8 10-8"/></svg>
        info@brightspanfacility.com
      </li>
      <li>
        <svg viewBox="0 0 24 24" fill="none" stroke="#1455a5" stroke-width="2"><circle cx="12" cy="12" r="10"/><path d="M2 12h20M12 2c3 3 3 17 0 20M12 2c-3 3-3 17 0 20"/></svg>
        <span>www.<span class="web-highlight">brightspanfacility</span>.com</span>
      </li>
    </ul>

    <p class="postal-address">PO Box 218, Larkfield Qld 4870</p>

    <div class="person">
      <p class="person-name">DANIEL MERCER</p>
      <p class="person-role">Managing Director</p>
    </div>

    <svg class="corner-stripes" viewBox="0 0 170 120" aria-hidden="true">
      <polygon points="170,0 170,18 62,120 38,120" fill="#666868"/>
      <polygon points="170,34 170,120 78,120" fill="#1455a5"/>
    </svg>
  </section>

</main>
</body>
</html>
```